Design the name for my Sailboat

I need a name to be designed for a sailboat that I just bought. The boat is a 1988 Pellham 25 Gullrunner. It is being re-painted: white with a blue stripe. We will sail it on Lake Thornmere near Dallas, TX. I would like the name on the stern next to the stairs and on the port and starboard sides of the hull. The name we have in mind is: "Carver Annalise". Carver is my son's middle name and Annalise is my wife's middle name. My wife is American and I am originally British (English). The TX registration # also needs to be incorporated on each side of the bow on the forward half of the vessel: TX-7415-KM. The designs will be printed onto decals at Bright Marks. The boat is 25' in length with an 8' beam.

Target Market(s)

Marine

Colors

Designer to choose colors to be used in the design.

Requirements
Must have
• Carver Annalise
Nice to have
• I am open to all suggestions. Maybe Anglo-American theme. Perhaps something related to TX or the Lone Star State.

```html
<!DOCTYPE html>
<html lang="en">
<head>
<meta charset="utf-8">
<title>Carver Annalise – Stern Name Decal</title>
<link rel="stylesheet" href="https://fonts.googleapis.com/css2?family=Archivo:wght@800&display=swap">
<style>
  :root {
    --page-bg: #eef0f2;
    --navy: #0b2a5b;
    --signal-red: #e3141b;
    --white: #ffffff;
    --foam: #f3f9fd;
    --sea-light: #d6ebf9;
    --sea-mid: #7fbcec;
    --sea-deep: #3f8fdc;
  }
  html, body {
    margin: 0;
    padding: 0;
    width: 867px;
    height: 1200px;
    overflow: hidden;
    background: var(--page-bg);
  }
  .canvas {
    position: relative;
    width: 867px;
    height: 1200px;
    display: flex;
    align-items: center;
    justify-content: center;
  }
  .stern-decal {
    width: 780px;
    height: auto;
    display: block;
    filter: drop-shadow(0 4px 8px rgba(0, 0, 0, 0.18));
  }
  .decal-name {
    font-family: "Archivo", "Arial Black", sans-serif;
    font-weight: 800;
    fill: var(--white);
  }
</style>
</head>
<body>
<main class="canvas">
  <svg class="stern-decal" viewBox="0 0 754 504" xmlns="http://www.w3.org/2000/svg" aria-label="Carver Annalise stern name decal">
    <defs>
      <clipPath id="decal-outline">
        <path d="M0,0 H754 V270 C754,420 650,504 540,504 H214 C104,504 0,420 0,270 Z"/>
      </clipPath>
      <linearGradient id="foam-fill" x1="0" y1="0" x2="0" y2="1">
        <stop offset="0" stop-color="var(--white)"/>
        <stop offset="1" stop-color="var(--foam)"/>
      </linearGradient>
      <linearGradient id="sea-tint" x1="0" y1="0" x2="1" y2="0">
        <stop offset="0" stop-color="var(--sea-light)"/>
        <stop offset="0.3" stop-color="var(--sea-mid)"/>
        <stop offset="0.55" stop-color="var(--sea-deep)"/>
        <stop offset="0.8" stop-color="var(--sea-mid)"/>
        <stop offset="1" stop-color="var(--sea-light)"/>
      </linearGradient>
      <linearGradient id="sea-fade" x1="0" y1="0" x2="0" y2="1">
        <stop offset="0" stop-color="#fff" stop-opacity="1"/>
        <stop offset="0.45" stop-color="#fff" stop-opacity="0.35"/>
        <stop offset="0.75" stop-color="#fff" stop-opacity="0.1"/>
        <stop offset="1" stop-color="#fff" stop-opacity="0.75"/>
      </linearGradient>
      <mask id="sea-mask">
        <rect x="0" y="330" width="754" height="174" fill="url(#sea-fade)"/>
      </mask>
    </defs>

    <g clip-path="url(#decal-outline)">
      <rect class="decal-base" x="0" y="0" width="754" height="504" fill="url(#foam-fill)"/>

      <rect class="splash-area" role="img" aria-label="Blue water splash illustration with droplets"
            x="-10" y="330" width="774" height="174" fill="url(#sea-tint)" mask="url(#sea-mask)"/>

      <path class="navy-field" fill="var(--navy)"
            d="M0,0 H754 V232 C640,238 520,222 400,188 C300,160 200,148 120,160 C70,168 30,185 0,200 Z"/>
      <path class="white-pinstripe" fill="var(--white)"
            d="M0,200 C30,185 70,168 120,160 C200,148 300,160 400,188 C520,222 640,238 754,232 V240 C640,246 520,230 400,196 C300,168 200,156 120,168 C70,176 30,193 0,210 Z"/>
      <path class="red-swoosh" fill="var(--signal-red)"
            d="M0,210 C30,193 70,176 120,168 C200,156 300,168 400,196 C520,230 640,246 754,240 V276 C640,278 560,270 470,240 C380,210 300,182 220,176 C130,170 60,210 0,265 Z"/>

      <text class="decal-name" x="377" y="117" font-size="86" text-anchor="middle" textLength="650" lengthAdjust="spacingAndGlyphs">Carver Annalise</text>
    </g>
  </svg>
</main>
</body>
</html>
```